We are looking for a new PowerPoint template for our new CI

Hey artmingle! For 25 years we have been an owner-managed IT system house with tradition, values and a great team. After more than 10 years, we would like to upgrade our company and design the entire CI contemporary and modern. Therefore we are looking for a Powerpoint Template which fits to our logo, the colors and an IT company. Details about our company and our service portfolio can be found on our homepage. We are currently adapting our homepage to the new CI resulting from the logo revision. Homepage: http://stage.kovantra.de Color codes: Gray = RGB: 4040404040 White = RGB: F5F5F5F5F5 Orange = RGB: F7931E Our slogan: We keep your system running Our address data: Company = Kovantra GmbH Street = Lindbergstraße 12 POSTCODE = 71844 City = Burladingen We look forward to your ideas and thank you all in advance.

Target Market(s)

Our target group are companies with 10 to 100 employees from all industrial sectors, eg https://www.morvik-werke.de/ https://www.faltner-logistik.de/ https://www.quensel.de/ de /

Colors

Designer to choose colors to be used in the design.

Requirements
Must have
• We are looking for a modern IT design in gray / orange. The basis of the design should be our logo. The template should have two different layouts and three different layouts for content. Our logo and slogan should be clearly visible on the start layout. In addition, an area should be reserved for the name of a speaker and the occasion of the presentation.

```html
<!DOCTYPE html>
<html lang="de">
<head>
<meta charset="utf-8">
<title>Kovantra – Business Presentation Template</title>
<link href="https://fonts.googleapis.com/css2?family=Oswald:wght@300;400;500&family=Roboto:wght@400;500;700&family=Archivo+Black&display=swap" rel="stylesheet">
<style>
:root{
  --orange:#f7931e;
  --orange-deep:#e8790c;
  --gray:#404040;
  --gray-mid:#8a8a8a;
  --gray-light:#bdbdbd;
  --white:#f5f5f5;
  --paper:#ffffff;
  --ink:#1e1e1e;
  --text:#555555;
}
*{margin:0;padding:0;box-sizing:border-box}
html,body{width:1200px;height:2201px;overflow:hidden;background:var(--paper)}
body{position:relative;font-family:"Roboto",Arial,sans-serif;color:var(--text)}

/* ---------- cover slide ---------- */
.cover{position:absolute;left:40px;top:40px;width:640px;height:360px;overflow:hidden;box-shadow:0 4px 14px rgba(0,0,0,.25)}
.cover-photo{position:absolute;inset:0;background:linear-gradient(120deg,#efe3cf 0%,#e6d3b6 45%,#d9c09d 70%,#eadcc6 100%)}
.cover-content{position:absolute;left:85px;top:92px}
.cover-brand{display:flex;align-items:center;gap:8px;font-family:"Oswald",sans-serif;font-weight:500;font-size:34px;line-height:1;color:var(--gray);letter-spacing:2px}
.brand-dot{width:14px;height:14px;background:var(--orange)}
.cover-title{font-family:"Oswald",sans-serif;font-weight:400;font-size:58px;line-height:.92;color:var(--gray);margin-top:8px;letter-spacing:-1px}
.cover-rule{width:460px;border-top:1.5px dashed var(--orange);margin-top:10px}
.cover-speaker{font-family:"Oswald",sans-serif;font-weight:300;font-size:16px;color:var(--orange-deep);margin-top:10px}
.cover-date{font-family:"Oswald",sans-serif;font-weight:300;font-size:12px;color:var(--gray)}

/* ---------- feature list ---------- */
.features{position:absolute;left:755px;top:28px;width:440px;font-family:"Archivo Black",sans-serif;font-size:21px;line-height:30px;color:var(--ink)}
.features li{list-style:none;position:relative;padding-left:24px}
.features li.main::before{content:"";position:absolute;left:2px;top:3px;width:17px;height:19px;border:3px solid var(--ink);border-radius:2px}
.features ul.sub{margin-left:58px}
.features ul.sub li{padding-left:20px}
.features ul.sub li::before{content:"";position:absolute;left:0;top:10px;width:8px;height:8px;background:var(--ink)}

/* ---------- slide frame ---------- */
.slide{position:absolute;width:484px;height:272px;background:var(--paper);box-shadow:2px 3px 8px rgba(0,0,0,.35);overflow:hidden}
.col-a{left:51px}.col-b{left:676px}
.row-1{top:462px}.row-2{top:751px}.row-3{top:1040px}.row-4{top:1328px}.row-5{top:1617px}.row-6{top:1905px}
.slide-head{position:absolute;left:0;top:0;height:30px;border-left:8px solid var(--orange);padding-left:8px;z-index:2}
.slide-title{font-family:"Oswald",sans-serif;font-weight:300;font-size:17px;line-height:20px;color:var(--ink);padding-top:4px;white-space:nowrap}
.slide-sub{font-family:"Oswald",sans-serif;font-weight:300;font-size:6.5px;color:var(--orange-deep);text-transform:uppercase;white-space:nowrap}
.logo{position:absolute;right:14px;top:11px;display:flex;align-items:center;gap:5px;font-family:"Oswald",sans-serif;font-weight:500;font-size:15px;line-height:1;letter-spacing:1.5px;color:var(--gray);z-index:2}
.logo .brand-dot{width:8px;height:8px}
.slide-foot{position:absolute;left:0;bottom:0;width:100%;height:14px;background:var(--ink);z-index:2}
.slide-foot span{position:absolute;right:0;top:0;width:140px;height:14px;background:var(--orange);font-family:"Oswald",sans-serif;font-weight:300;font-size:6.5px;line-height:14px;color:#fff;text-align:right;padding-right:4px}

.photo{position:absolute;background:linear-gradient(135deg,#c9c9c9,#8f8f8f)}
.photo.warm{background:linear-gradient(135deg,#f6b15a,#d9781a)}
.photo.sky{background:linear-gradient(180deg,#8fb6dc,#a9b97a 70%,#7f9850)}
.photo.office{background:linear-gradient(135deg,#d9dde2,#9aa3ad)}
.photo.box{background:linear-gradient(160deg,#fbd34d,#f0a11a 60%,#e6e6e6 61%,#cfcfcf)}
.photo.people{background:linear-gradient(135deg,#e3e6ea,#b8c1cc)}
.photo.sunset{background:linear-gradient(180deg,#e0600e,#f59324 70%,#2b1606 71%)}
.photo.crystal{background:linear-gradient(180deg,#b9cde0,#d5b591 60%,#9a7a55)}
.photo.car{background:linear-gradient(180deg,#3b77c9,#9fb0c4)}
.photo.street{background:linear-gradient(135deg,#5b6b7a,#c2c7cc)}
.stripe{position:absolute;width:4px;background:var(--orange)}

.h-sub{position:absolute;font-family:"Oswald",sans-serif;font-weight:300;font-size:8.5px;line-height:10px;color:var(--orange-deep);text-transform:uppercase;border-bottom:1px dashed var(--orange);padding-bottom:1px}
.txt{position:absolute;font-size:6.3px;line-height:8.4px;color:var(--text)}
.txt p+p{margin-top:4px}
.txt em{font-style:normal;color:var(--orange-deep)}
.txt.just{text-align:justify}

/* slide specific */
.concept-band-label{position:absolute;left:60px;top:170px;width:110px;text-align:right;font-family:"Oswald",sans-serif;font-weight:300;font-size:8px;color:#fff;border-bottom:2px solid var(--orange);padding-bottom:2px}
.concept-text{color:#fff}
.vision-title{position:absolute;left:0;top:130px;width:170px;text-align:right;font-family:"Oswald",sans-serif;font-weight:300;font-size:23px;color:var(--ink);border-bottom:2.5px solid var(--orange);padding-right:2px}
.icon{position:absolute;width:54px;height:54px}
.person-name{position:absolute;font-weight:700;font-size:10px;color:var(--orange-deep);border-bottom:1px dashed var(--orange);padding-bottom:1px}
.person-body{font-size:7.5px;line-height:17px;color:var(--ink)}
.chart{position:absolute;left:18px;top:78px;width:220px;height:150px}
.donut{position:absolute;width:100px;height:100px}
</style>
</head>
<body>

<!-- Cover -->
<section class="cover">
  <div class="cover-photo" role="img" aria-label="Faded warm-toned background photo of a man in front of a lettered wall"></div>
  <div class="cover-content">
    <div class="cover-brand"><span class="brand-dot"></span>KOVANTRA</div>
    <h1 class="cover-title">BUSINESS<br>PRESENTATION</h1>
    <div class="cover-rule"></div>
    <div class="cover-speaker">JONAS REITER</div>
    <div class="cover-date">15 DECEMBER 2019</div>
  </div>
</section>

<!-- Feature list -->
<ul class="features">
  <li class="main">Ratio 16:9</li>
  <li class="main">Full HD</li>
  <li class="main">Custom color pallet</li>
  <li class="main">Custom Font -&nbsp; Easy Change</li>
  <li class="main">Easy to edit, just drag and drop images</li>
  <li class="main">Can be included up to 50 slides;
    <ul class="sub">
      <li>Text + images (1,2,3,4) , Text Slides</li>
      <li>Portfolio Slides , blog slides</li>
      <li>Text Slides, infographics</li>
      <li>Data Slides</li>
    </ul>
  </li>
  <li class="main">In the sample you find 13 slides</li>
</ul>

<!-- 1 Main concept -->
<section class="slide col-a row-1">
  <div class="photo warm" style="left:0;top:0;width:484px;height:258px" role="img" aria-label="Orange-toned photo of a smiling support agent with headset at a laptop"></div>
  <div class="slide-head"><div class="slide-title">MAIN CONCEPT</div><div class="slide-sub">Lorem ipsum dolor sit amet</div></div>
  <div class="logo"><span class="brand-dot"></span>KOVANTRA</div>
  <div class="concept-band-label">LOREM IPSUM DOLOR SIT AMET</div>
  <div class="txt concept-text" style="left:177px;top:168px;width:285px"><p>Lorem ipsum dolor sit amet, consectetur adipisicing elit, sed do eiusmod tempor incididunt ut labore et dolore magna aliqua. Ut enim ad minim veniam, quis nostrud exercitation ullamco laboris nisi ut aliquip ex ea commodo consequat.</p><p>Duis aute irure dolor in reprehenderit in voluptate velit esse cillum dolore eu fugiat nulla pariatur. Excepteur sint occaecat cupidatat non proident, sunt in culpa qui officia deserunt mollit anim id est laborum.</p></div>
  <div class="slide-foot"><span>PRESENTATION TITLE HERE</span></div>
</section>

<!-- 2 Our company -->
<section class="slide col-b row-1">
  <div class="slide-head"><div class="slide-title">OUR COMPANY</div><div class="slide-sub">Lorem ipsum dolor sit amet</div></div>
  <div class="logo"><span class="brand-dot"></span>KOVANTRA</div>
  <div class="stripe" style="left:20px;top:65px;height:157px"></div>
  <div class="photo box" style="left:60px;top:72px;width:110px;height:140px" role="img" aria-label="Orange software product box"></div>
  <div class="h-sub" style="left:190px;top:70px;width:282px">SUB TITLE</div>
  <div class="txt" style="left:190px;top:85px;width:282px">Lorem ipsum dolor sit amet, consectetur adipisicing elit, sed do eiusmod tempor incididunt ut labore et dolore magna aliqua. Ut enim ad minim veniam, quis nostrud exercitation ullamco laboris nisi ut aliquip ex ea commodo consequat.</div>
  <div class="h-sub" style="left:190px;top:150px;width:282px">SUB TITLE</div>
  <div class="txt" style="left:190px;top:165px;width:282px"><p>Duis aute irure dolor in reprehenderit in voluptate velit esse cillum dolore eu fugiat nulla pariatur.</p><p>Excepteur sint occaecat cupidatat non proident, sunt in culpa qui officia deserunt mollit anim id est laborum.</p></div>
  <div class="slide-foot"><span>PRESENTATION TITLE HERE</span></div>
</section>

<!-- 3 Our vision -->
<section class="slide col-a row-2">
  <div class="slide-head"><div class="slide-title">OUR VISION</div><div class="slide-sub">Lorem ipsum dolor sit amet</div></div>
  <div class="vision-title">OUR VISION</div>
  <div class="txt" style="left:190px;top:132px;width:285px"><p>Lorem ipsum dolor sit amet, consectetur adipisicing elit, sed do eiusmod tempor incididunt ut labore et dolore magna aliqua. Ut enim ad minim veniam, quis nostrud exercitation <em>ullamco laboris nisi ut aliquip</em> ex ea commodo consequat.</p><p>Duis aute irure dolor in reprehenderit in voluptate velit esse cillum dolore eu fugiat nulla pariatur. Excepteur sint occaecat cupidatat non proident, sunt in culpa qui officia deserunt mollit anim id est laborum.</p></div>
  <div class="slide-foot"><span>PRESENTATION TITLE HERE</span></div>
</section>

<!-- 4 Psychische Belastungen -->
<section class="slide col-b row-2">
  <div class="slide-head"><div class="slide-title">PSYCHISCHE BELASTUNGEN</div><div class="slide-sub">Im Zeitraum von 2006 bis 2016 sind die psychischen Erkrankungen der Arbeitnehmer um fast 100%</div></div>
  <div class="logo"><span class="brand-dot"></span>KOVANTRA</div>
  <svg class="icon" style="left:48px;top:65px" viewBox="0 0 54 54" fill="none" stroke="#f7931e"><circle cx="27" cy="27" r="25" stroke-width="2"/><path d="M16 27l8 8 15-17" stroke-width="4" stroke-linecap="round" stroke-linejoin="round"/></svg>
  <svg class="icon" style="left:160px;top:65px" viewBox="0 0 54 54" fill="none" stroke="#f7931e"><circle cx="27" cy="27" r="25" stroke-width="2"/><path d="M27 12l12 5v9c0 8-5 13-12 16-7-3-12-8-12-16v-9z" fill="#f7931e"/><circle cx="27" cy="24" r="3.5" fill="#fff" stroke="none"/><path d="M20.5 33c1.5-4 11.5-4 13 0" stroke="#fff" stroke-width="3"/></svg>
  <svg class="icon" style="left:272px;top:65px" viewBox="0 0 54 54" fill="none" stroke="#f7931e"><circle cx="27" cy="27" r="25" stroke-width="2"/><circle cx="31" cy="23" r="8" stroke-width="3"/><path d="M25 29l-10 10" stroke-width="4" stroke-linecap="round"/></svg>
  <svg class="icon" style="left:384px;top:65px" viewBox="0 0 54 54" fill="none" stroke="#f7931e"><circle cx="27" cy="27" r="25" stroke-width="2"/><circle cx="27" cy="30" r="10" stroke-width="3"/><path d="M27 30v-6M24 16h6M27 16v4M36 20l2-2" stroke-width="2.5" stroke-linecap="round"/></svg>
  <div class="h-sub" style="left:24px;top:146px;width:95px">EINFACHE ERMITTLUNG</div>
  <div class="h-sub" style="left:136px;top:136px;width:95px">ERKENNEN VON<br>BELASTUNGEN</div>
  <div class="h-sub" style="left:248px;top:136px;width:95px">TRANSPARENTE<br>DARSTELLUNG</div>
  <div class="h-sub" style="left:360px;top:146px;width:95px">SCHNELLE ERGEBNISSE</div>
  <div class="txt" style="left:24px;top:162px;width:95px">Lorem ipsum dolor sit amet, consectetur adipisicing elit, sed do eiusmod tempor incididunt ut labore et dolore magna aliqua. Ut enim ad minim veniam, quis nostrud exercitation</div>
  <div class="txt" style="left:136px;top:162px;width:95px">Lorem ipsum dolor sit amet, consectetur adipisicing elit, sed do eiusmod tempor incididunt ut labore et dolore magna aliqua. Ut enim ad minim veniam, quis nostrud exercitation</div>
  <div class="txt" style="left:248px;top:162px;width:95px">Lorem ipsum dolor sit amet, consectetur adipisicing elit, sed do eiusmod tempor incididunt ut labore et dolore magna aliqua. Ut enim ad minim veniam, quis nostrud exercitation</div>
  <div class="txt" style="left:360px;top:162px;width:95px">Lorem ipsum dolor sit amet, consectetur adipisicing elit, sed do eiusmod tempor incididunt ut labore et dolore magna aliqua. Ut enim ad minim veniam, quis nostrud exercitation</div>
  <div class="slide-foot"><span>PRESENTATION TITLE HERE</span></div>
</section>

<!-- 5 Arbeitsschutz -->
<section class="slide col-a row-3">
  <div class="slide-head"><div class="slide-title">ARBEITSSCHUTZ - MANAGEMENT SOFTWARE</div><div class="slide-sub">Lorem ipsum dolor sit amet</div></div>
  <div class="logo"><span class="brand-dot"></span>KOVANTRA</div>
  <div class="photo sunset" style="left:24px;top:56px;width:103px;height:99px" role="img" aria-label="Orange sunset over a dark horizon"></div>
  <div class="photo street" style="left:136px;top:56px;width:103px;height:99px" role="img" aria-label="Young man with sunglasses and cap outdoors"></div>
  <div class="photo crystal" style="left:249px;top:56px;width:103px;height:99px" role="img" aria-label="Hand holding a clear crystal over a landscape"></div>
  <div class="photo car" style="left:361px;top:56px;width:103px;height:99px" role="img" aria-label="Silver sports car with open gull-wing doors"></div>
  <div class="h-sub" style="left:24px;top:162px;width:103px">EINFACH</div>
  <div class="h-sub" style="left:136px;top:162px;width:103px">SICHER</div>
  <div class="h-sub" style="left:249px;top:162px;width:103px">TRANSPARENT</div>
  <div class="h-sub" style="left:361px;top:162px;width:103px">SCHNELL</div>
  <div class="txt" style="left:24px;top:176px;width:103px">Lorem ipsum dolor sit amet, consectetur adipisicing elit, sed do eiusmod tempor incididunt ut labore et dolore magna aliqua.</div>
  <div class="txt" style="left:136px;top:176px;width:103px">Duis aute irure dolor in reprehenderit in voluptate velit esse cillum dolore eu fugiat nulla pariatur.</div>
  <div class="txt" style="left:249px;top:176px;width:103px">Lorem ipsum dolor sit amet, consectetur adipisicing elit, sed do eiusmod tempor incididunt ut labore et dolore magna aliqua.</div>
  <div class="txt" style="left:361px;top:176px;width:103px">Duis aute irure dolor in reprehenderit in voluptate velit esse cillum dolore eu fugiat nulla pariatur.</div>
  <div class="slide-foot"><span>PRESENTATION TITLE HERE</span></div>
</section>

<!-- 6 Vertriebsleiter -->
<section class="slide col-b row-3">
  <div class="slide-head"><div class="slide-title">LERNEN SIE UNSEREN VERTRIEBSLEITER</div><div class="slide-sub">Prokurist, kennen</div></div>
  <div class="logo"><span class="brand-dot"></span>KOVANTRA</div>
  <div class="stripe" style="left:19px;top:64px;height:157px"></div>
  <div class="photo people" style="left:23px;top:64px;width:160px;height:157px" role="img" aria-label="Portrait photo of the head of sales in a white shirt"></div>
  <div class="person-name" style="left:190px;top:66px;width:285px">Jonas Reiter</div>
  <div class="txt person-body" style="left:190px;top:78px;width:280px">Leitung Vertrieb, Prokurist<br>Als Familienunternehmen in 2. Generation unterstützen wir seit über 25 Jahren zahlreiche Kunden in Sachen IT und im Bereich der Softwareentwicklung. Auf unsere Zusammenarbeit und Ihre Kontaktaufnahme freue ich mich schon jetzt!<br>07471 55 20 300 oder sales@kovantra.de</div>
  <div class="slide-foot"><span>PRESENTATION TITLE HERE</span></div>
</section>

<!-- 7 Leistung & Service -->
<section class="slide col-a row-4">
  <div class="slide-head"><div class="slide-title">LEISTUNG &amp; SERVICE</div><div class="slide-sub">Softwareentwicklung, IT Systemhaus und technischer Support</div></div>
  <div class="logo"><span class="brand-dot"></span>KOVANTRA</div>
  <div class="stripe" style="left:39px;top:56px;height:95px"></div>
  <div class="photo box" style="left:43px;top:56px;width:91px;height:95px" role="img" aria-label="Orange software product box"></div>
  <div class="photo sky" style="left:191px;top:56px;width:102px;height:95px" role="img" aria-label="Green hilly landscape under blue sky"></div>
  <div class="stripe" style="left:340px;top:56px;height:95px"></div>
  <div class="photo office" style="left:344px;top:56px;width:98px;height:95px" role="img" aria-label="Support agent with headset at a laptop"></div>
  <div class="h-sub" style="left:41px;top:160px;width:118px">ARBEITSSCHUTZ<br>MANAGEMENT SOFTWARE</div>
  <div class="h-sub" style="left:191px;top:160px;width:118px">IT SYSTEMHAUS - IHR<br>PARTNER IN DER REGION</div>
  <div class="h-sub" style="left:340px;top:170px;width:118px">TECHNISCHER SUPPORT</div>
  <div class="txt" style="left:41px;top:190px;width:118px">Mit unserer Arbeitsschutz-Software werden Ihre Vorgesetzten, Fachkräfte für Arbeitssicherheit, Administratoren und Kontrollorgane entlastet und unterstützt.</div>
  <div class="txt" style="left:191px;top:190px;width:118px">Drei Säulen bilden die Basis für die Zufriedenheit unserer Kunden: Die individuelle IT-Beratung, perfekte IT-Lösungen für jeden Anspruch im Bereich Hard- und Software sowie IT-Service der über eine reine</div>
  <div class="txt" style="left:340px;top:190px;width:118px">Immer auf der sicheren Seite: Egal ob Fernwartung oder direkt Vor-Ort - mit unseren Wartungs- und Serviceangeboten. Transparent und fair durch eigenes Ticket/CRM-System.</div>
  <div class="slide-foot"><span>PRESENTATION TITLE HERE</span></div>
</section>

<!-- 8 About us -->
<section class="slide col-b row-4">
  <div class="slide-head"><div class="slide-title">ABOUT US</div><div class="slide-sub">Meet our Leitung Vertrieb, Prokurist</div></div>
  <div class="logo"><span class="brand-dot"></span>KOVANTRA</div>
  <div class="stripe" style="left:19px;top:64px;height:157px"></div>
  <div class="photo people" style="left:23px;top:64px;width:160px;height:157px" role="img" aria-label="Photo of two business partners standing side by side"></div>
  <div class="h-sub" style="left:190px;top:66px;width:285px">JONAS AND FELIX</div>
  <div class="txt just" style="left:190px;top:80px;width:285px"><p>Lorem ipsum dolor sit amet, consectetur adipisicing elit, sed do eiusmod tempor incididunt ut labore et dolore magna aliqua. Ut enim ad minim veniam, quis nostrud exercitation ullamco laboris nisi ut aliquip ex ea commodo consequat.</p><p>Duis aute irure dolor in reprehenderit in voluptate velit esse cillum dolore eu fugiat nulla pariatur. Excepteur sint occaecat cupidatat non proident, sunt in culpa qui officia deserunt mollit anim id est laborum.</p><p>Lorem ipsum dolor sit amet, consectetur adipisicing elit, sed do eiusmod tempor incididunt ut labore et dolore magna aliqua. Ut enim ad minim veniam, quis nostrud exercitation ullamco laboris nisi ut aliquip ex ea commodo consequat.</p><p>Duis aute irure dolor in reprehenderit in voluptate velit esse cillum dolore eu fugiat nulla pariatur. Excepteur sint occaecat cupidatat non proident, sunt in culpa qui officia deserunt mollit anim id est laborum.</p></div>
  <div class="slide-foot"><span>PRESENTATION TITLE HERE</span></div>
</section>

<!-- 9 Our services -->
<section class="slide col-a row-5">
  <div class="slide-head"><div class="slide-title">OUR SERVICES</div></div>
  <div class="logo"><span class="brand-dot"></span>KOVANTRA</div>
  <div class="photo street" style="left:40px;top:56px;width:179px;height:99px" role="img" aria-label="Man in front of a colourful lettered wall"></div>
  <div class="photo office" style="left:265px;top:56px;width:179px;height:99px" role="img" aria-label="Hands typing on a laptop keyboard"></div>
  <div class="txt" style="left:45px;top:178px;width:175px">Lorem ipsum dolor sit amet, consectetur adipisicing elit, sed do eiusmod tempor incididunt ut labore et dolore magna aliqua. Ut enim ad minim veniam, quis nostrud exercitation ullamco laboris nisi ut aliquip ex ea commodo consequat.</div>
  <div class="txt" style="left:269px;top:178px;width:175px">Lorem ipsum dolor sit amet, consectetur adipisicing elit, sed do eiusmod tempor incididunt ut labore et dolore magna aliqua. Ut enim ad minim veniam, quis nostrud exercitation ullamco laboris nisi ut aliquip ex ea commodo consequat.</div>
  <div class="slide-foot"><span>PRESENTATION TITLE HERE</span></div>
</section>

<!-- 10 Pillars -->
<section class="slide col-b row-5">
  <div class="slide-head"><div class="slide-title">3 IMPRESSIVE PILLARS</div><div class="slide-sub">Lorem ipsum dolor sit amet</div></div>
  <div class="logo"><span class="brand-dot"></span>KOVANTRA</div>
  <div class="h-sub" style="left:26px;top:60px;width:131px">REBORN</div>
  <div class="h-sub" style="left:176px;top:60px;width:131px">REUNITE</div>
  <div class="h-sub" style="left:327px;top:60px;width:131px">REINFORCE</div>
  <div class="txt" style="left:26px;top:74px;width:131px;font-size:6px;line-height:7.8px"><p>Lorem ipsum dolor sit amet, consectetur adipisicing elit, sed do eiusmod tempor incididunt ut labore et dolore magna aliqua. Ut enim ad minim veniam, quis nostrud exercitation ullamco laboris nisi ut aliquip ex ea commodo consequat.</p><p><em>Duis aute irure</em> dolor in reprehenderit in voluptate velit esse cillum dolore eu fugiat nulla pariatur. Excepteur sint occaecat cupidatat non proident, sunt in culpa qui officia deserunt mollit anim id est laborum.</p></div>
  <div class="txt" style="left:176px;top:74px;width:131px;font-size:6px;line-height:7.8px"><em>Sed ut perspiciatis</em>, unde omnis iste natus error sit voluptatem accusantium doloremque laudantium, totam rem aperiam eaque ipsa, quae ab illo inventore veritatis et quasi <em>architecto beatae vitae dicta sunt</em>, explicabo. Nemo enim ipsam voluptatem, quia voluptas sit, aspernatur aut odit aut fugit, sed quia consequuntur magni dolores eos, qui ratione voluptatem sequi nesciunt, neque porro quisquam est, qui dolorem ipsum, quia dolor sit amet consectetur adipisci velit, sed quia non numquam eius modi tempora incidunt, ut labore et dolore magnam aliquam quaerat voluptatem.</div>
  <div class="txt" style="left:327px;top:74px;width:131px;font-size:6px;line-height:7.8px"><p>At vero eos et accusamus et iusto odio dignissimos ducimus, qui blanditiis praesentium voluptatum deleniti atque corrupti, quos dolores et quas molestias excepturi sint, obcaecati <em>cupiditate non provident</em>, similique sunt in culpa, qui officia deserunt mollitia animi, id est laborum et dolorum fuga.</p><p><em>Et harum quidem rerum</em> facilis est et expedita distinctio. Nam libero tempore, cum soluta nobis est eligendi optio, cumque nihil impedit, quo minus id, quod maxime placeat, facere possimus, omnis voluptas assumenda est, omnis dolor repellendus.</p></div>
  <div class="slide-foot"><span>PRESENTATION TITLE HERE</span></div>
</section>

<!-- 11 Sales and purchases -->
<section class="slide col-a row-6">
  <div class="slide-head"><div class="slide-title">SALES AND PURCHASES</div><div class="slide-sub">Lorem ipsum dolor sit amet</div></div>
  <div class="logo"><span class="brand-dot"></span>KOVANTRA</div>
  <svg class="chart" viewBox="0 0 220 150" font-family="Roboto, sans-serif" font-size="4.5" fill="#444">
    <g text-anchor="end">
      <text x="10" y="12">120</text><text x="10" y="30">100</text><text x="10" y="48">80</text><text x="10" y="66">60</text><text x="10" y="84">40</text><text x="10" y="102">20</text><text x="10" y="120">0</text>
    </g>
    <g fill="#a6a6a6">
      <rect x="20" y="78" width="7" height="40"/><rect x="36" y="68" width="7" height="50"/><rect x="52" y="83" width="7" height="35"/><rect x="68" y="86" width="7" height="32"/><rect x="84" y="58" width="7" height="60"/><rect x="100" y="69" width="7" height="49"/><rect x="116" y="50" width="7" height="68"/><rect x="132" y="47" width="7" height="71"/><rect x="148" y="43" width="7" height="75"/><rect x="164" y="35" width="7" height="83"/><rect x="180" y="38" width="7" height="80"/><rect x="196" y="34" width="7" height="84"/>
    </g>
    <polyline fill="none" stroke="#f7931e" stroke-width="1.2" points="23.5,72 39.5,70 55.5,64 71.5,75 87.5,73 103.5,80 119.5,70 135.5,52 151.5,39 167.5,31 183.5,37 199.5,48"/>
    <g fill="#f7931e"><circle cx="39.5" cy="70" r="1.6"/><circle cx="55.5" cy="64" r="1.6"/><circle cx="71.5" cy="75" r="1.6"/><circle cx="135.5" cy="52" r="1.6"/><circle cx="167.5" cy="31" r="1.6"/><circle cx="199.5" cy="48" r="1.6"/></g>
    <g text-anchor="middle">
      <text x="23.5" y="128">JAN</text><text x="39.5" y="128">FEB</text><text x="55.5" y="128">MAR</text><text x="71.5" y="128">APR</text><text x="87.5" y="128">MAY</text><text x="103.5" y="128">JUN</text><text x="119.5" y="128">JUL</text><text x="135.5" y="128">AUG</text><text x="151.5" y="128">SEP</text><text x="167.5" y="128">OCT</text><text x="183.5" y="128">NOV</text><text x="199.5" y="128">DEC</text>
    </g>
    <rect x="84" y="137" width="4" height="3" fill="#a6a6a6"/><text x="90" y="140" font-size="4">SALES</text>
    <line x1="103" y1="138.5" x2="108" y2="138.5" stroke="#f7931e"/><text x="110" y="140" font-size="4">PURCHASES</text>
  </svg>
  <div class="h-sub" style="left:242px;top:85px;width:218px">WINTER SALES</div>
  <div class="txt" style="left:242px;top:99px;width:218px"><p>Lorem ipsum dolor sit amet, consectetur adipisicing elit, sed do eiusmod tempor <em>incididunt ut labore</em> et dolore magna aliqua. Ut enim ad minim veniam, quis nostrud exercitation ullamco laboris nisi ut aliquip ex ea commodo consequat.</p><p>Duis aute irure dolor in <em>reprehenderit in voluptate</em> velit esse cillum dolore eu fugiat nulla pariatur. Excepteur sint occaecat cupidatat non proident, sunt in culpa qui officia deserunt mollit anim id est laborum.</p></div>
  <div class="slide-foot"><span>PRESENTATION TITLE HERE</span></div>
</section>

<!-- 12 Positive / negative -->
<section class="slide col-b row-6">
  <div class="slide-head"><div class="slide-title">POSITIVE? NEGATIVE?</div><div class="slide-sub">Lorem ipsum dolor sit amet</div></div>
  <div class="logo"><span class="brand-dot"></span>KOVANTRA</div>
  <svg class="donut" style="left:42px;top:52px" viewBox="0 0 100 100"><circle cx="50" cy="50" r="42" fill="none" stroke="#404040" stroke-width="10"/><circle cx="50" cy="50" r="42" fill="none" stroke="#f7931e" stroke-width="10" stroke-dasharray="205.8 263.9" transform="rotate(-90 50 50)"/><text x="50" y="58" text-anchor="middle" font-family="Oswald, sans-serif" font-weight="300" font-size="22" fill="#1e1e1e">78%</text></svg>
  <svg class="donut" style="left:192px;top:52px" viewBox="0 0 100 100"><circle cx="50" cy="50" r="42" fill="none" stroke="#404040" stroke-width="10"/><circle cx="50" cy="50" r="42" fill="none" stroke="#f7931e" stroke-width="10" stroke-dasharray="237.5 263.9" transform="rotate(-90 50 50)"/><text x="50" y="58" text-anchor="middle" font-family="Oswald, sans-serif" font-weight="300" font-size="22" fill="#1e1e1e">90%</text></svg>
  <svg class="donut" style="left:342px;top:52px" viewBox="0 0 100 100"><circle cx="50" cy="50" r="42" fill="none" stroke="#404040" stroke-width="10"/><circle cx="50" cy="50" r="42" fill="none" stroke="#f7931e" stroke-width="10" stroke-dasharray="227 263.9" transform="rotate(-90 50 50)"/><text x="50" y="58" text-anchor="middle" font-family="Oswald, sans-serif" font-weight="300" font-size="22" fill="#1e1e1e">86%</text></svg>
  <div class="h-sub" style="left:42px;top:166px;width:100px">TOKYO</div>
  <div class="h-sub" style="left:192px;top:166px;width:100px">PARIS</div>
  <div class="h-sub" style="left:342px;top:166px;width:100px">NEW YORK</div>
  <div class="txt" style="left:42px;top:180px;width:100px">Lorem ipsum dolor sit amet, consectetur adipisicing elit, sed do eiusmod tempor incididunt ut labore et dolore magna aliqua.</div>
  <div class="txt" style="left:192px;top:180px;width:100px">Duis aute irure dolor in reprehenderit in voluptate velit esse cillum dolore eu fugiat nulla pariatur.</div>
  <div class="txt" style="left:342px;top:180px;width:100px">Lorem ipsum dolor sit amet, consectetur adipisicing elit, sed do eiusmod tempor incididunt ut labore et dolore magna aliqua.</div>
  <div class="slide-foot"><span>PRESENTATION TITLE HERE</span></div>
</section>

</body>
</html>
```